Harwick Legal

To update and modernize current business card appearance. Marta's business is based in Melbourne with 4 other lawyers in the firm. Marta travels to the Pilbara in Western Australia approximately 1 week a month as part of the firms legal work. She consults with clients in Newman, Tom Price and Port Hedland. The lawyers work mostly from a home office, apart from court appearances. They have a virtual office in Melbourne city, and use facilities in 3 or 4 other locations around Melbourne. It is important the client's think this is a conventional law firm with a permanent office. Our business structure is a difficult concept for them to grasp. The business has been operational for 3 years, growing from 1 lawyer to 4 lawyers during that time. Our website is www.Harwicklegal.example.au and is currently being upgraded as we are not happy with its content. The logo is currently orange and dark grey but the orange is a difficult colour to reproduce and often turns out "poo" brown when documents are printed. We need clients to know we are user friendly and caring - and not head up our rears ends as some lawyers appear to be.
Updates

Thank you for the feedback so far. 1. Some of the designs have too much black (We prefer darker grey & not too much.) 2. Happy for designers to play around with different colours & logo design. What we're after is a modern look and business card that people say "wow" when they pick it up.

Industry/Entity Type

Business

```html
<!DOCTYPE html>
<html lang="en">
<head>
<meta charset="utf-8">
<title>Harwick Legal – Business Card</title>
<link rel="stylesheet" href="https://fonts.googleapis.com/css2?family=EB+Garamond:wght@400;600;700&family=Source+Sans+3:wght@400&display=swap">
<style>
  :root {
    --canvas: #d3d4d6;
    --card: #efefef;
    --ink: #1a1a1a;
    --grey: #5e5f61;
    --muted: #7a7a7a;
    --red: #a3161c;
    --serif: "EB Garamond", Garamond, serif;
    --sans: "Source Sans 3", Arial, sans-serif;
  }
  * { margin: 0; padding: 0; box-sizing: border-box; }
  html, body { width: 1200px; height: 1200px; overflow: hidden; }
  body { background: var(--canvas); font-family: var(--serif); color: var(--ink); position: relative; }

  .card {
    position: absolute; left: 216px; width: 764px; height: 462px;
    background: var(--card);
    box-shadow: 0 2px 6px rgba(0,0,0,0.15);
  }
  .card--front { top: 130px; }
  .card--back { top: 600px; }

  .abs { position: absolute; white-space: nowrap; }

  .tagline { left: 31px; top: 16px; font-size: 21px; letter-spacing: 0.06em; word-spacing: 0.35em; }

  .brand { display: flex; align-items: center; gap: 12px; }
  .brand__dot { width: 22px; height: 22px; border-radius: 50%; background: var(--red); flex: none; }
  .brand__name { font-family: var(--serif); font-weight: 400; color: var(--grey); font-size: 44px; letter-spacing: 0.04em; }
  .card--front .brand { left: 62px; top: 196px; }
  .card--back .brand { left: 42px; top: 206px; }
  .card--back .brand__name { font-size: 38px; }
  .card--back .brand__dot { width: 18px; height: 18px; }

  .services { left: 450px; top: 235px; font-size: 23px; line-height: 27px; }
  .services__head { font-weight: 700; font-size: 24px; margin-bottom: 2px; }
  .services__head--gap { margin-top: 8px; }
  .front-web { left: 450px; top: 418px; font-size: 22px; }

  .identity { right: 54px; top: 22px; text-align: right; }
  .identity__name { font-weight: 700; font-size: 33px; line-height: 38px; }
  .identity__creds { font-size: 17px; color: var(--muted); margin-top: 2px; }
  .identity__role { font-size: 28px; margin-top: 6px; }

  .contacts { right: 32px; top: 295px; list-style: none; }
  .contacts li { display: flex; justify-content: flex-end; align-items: center; gap: 12px; font-family: var(--sans); font-size: 22px; height: 32px; }
  .contacts li.contacts__web { margin-top: 22px; font-family: var(--serif); }
  .contacts svg { width: 20px; height: 20px; flex: none; }
</style>
</head>
<body>

<section class="card card--front">
  <p class="abs tagline">EXPERIENCE SUPPORT SOLUTIONS</p>
  <div class="abs brand">
    <span class="brand__dot"></span>
    <span class="brand__name">Harwick Legal</span>
  </div>
  <div class="abs services">
    <p class="services__head">Family Law</p>
    <p>Collaborative Practice</p>
    <p>Mediation &amp; Negotiation</p>
    <p>Intervention Orders</p>
    <p class="services__head services__head--gap">Criminal Law</p>
  </div>
  <p class="abs front-web">www.Harwicklegal.example.au</p>
</section>

<section class="card card--back">
  <div class="abs identity">
    <p class="identity__name">J. Marta Corliss</p>
    <p class="identity__creds">LLB(Hons) - Accredited Mediator</p>
    <p class="identity__role">Principal Solicitor</p>
  </div>
  <div class="abs brand">
    <span class="brand__dot"></span>
    <span class="brand__name">Harwick Legal</span>
  </div>
  <ul class="abs contacts">
    <li>1300 Harwick (427 942)
      <svg viewBox="0 0 20 20" aria-hidden="true"><circle cx="10" cy="10" r="10" fill="#fff"/><path d="M6 5c1-1 2 0 2.5 1.5s-.5 1.5-.5 2 2 3 2.5 3.3.8-.7 1.5-.6 2.3 1.3 1.6 2.3-2 1.5-4-.2S4 7 6 5z" fill="var(--red)"/></svg>
    </li>
    <li>0400 555 018
      <svg viewBox="0 0 20 20" aria-hidden="true"><circle cx="10" cy="10" r="10" fill="#fff"/><rect x="6.5" y="3.5" width="7" height="13" rx="1.2" fill="var(--red)"/><rect x="7.8" y="5" width="4.4" height="7" fill="#fff"/></svg>
    </li>
    <li>marta.corliss@harwicklegal.example.au
      <svg viewBox="0 0 20 20" aria-hidden="true"><circle cx="10" cy="10" r="10" fill="#fff"/><rect x="3.5" y="6" width="13" height="9" fill="var(--red)"/><path d="M3.5 6l6.5 5 6.5-5" fill="none" stroke="#fff" stroke-width="1.2"/></svg>
    </li>
    <li class="contacts__web">www.Harwicklegal.example.au
      <svg viewBox="0 0 20 20" aria-hidden="true"><circle cx="10" cy="10" r="7.5" fill="none" stroke="var(--red)" stroke-width="1.6"/><ellipse cx="10" cy="10" rx="3.2" ry="7.5" fill="none" stroke="var(--red)" stroke-width="1.3"/><path d="M2.5 10h15M4 6h12M4 14h12" stroke="var(--red)" stroke-width="1.2"/></svg>
    </li>
  </ul>
</section>

</body>
</html>
```